LOGO for A Neighborhood Finance Center
BLUE LEDGER PLUS
Professional
HAROLD QUINCE and DENNIS HOLTBERG
Manger
3710 S Wexford st 204
Fairbrook ST 00000
BlueLEDGERPLUS@mailnook.example
BLUELEDGERPLUS.example
I need two versions one with Harold Quince
I need one with Dennis Holtberg

```html
<!DOCTYPE html>
<html lang="en">
<head>
<meta charset="utf-8">
<title>Blue Ledger Plus – Business Cards</title>
<link rel="stylesheet" href="https://fonts.googleapis.com/css2?family=Open+Sans:wght@400;600;700&display=swap">
<style>
  :root{
    --bg:#e9ebee;
    --card-white:#ffffff;
    --card-frost:#eef2f4;
    --blue-dark:#0d4f9e;
    --blue-mid:#1d6fc8;
    --blue-light:#3a8ee0;
    --silver:#c9d3dc;
    --brand:#1c64b8;
    --brand-dot:#7cbf3a;
    --text-light:#ffffff;
  }
  *{box-sizing:border-box;margin:0;padding:0}
  html,body{width:1200px;height:730px;overflow:hidden}
  body{background:var(--bg);font-family:"Open Sans",Arial,sans-serif;position:relative}

  .card{
    position:absolute;width:462px;height:272px;border-radius:16px;overflow:hidden;
    box-shadow:0 6px 18px rgba(0,0,0,.18);
    display:flex;flex-direction:column;
  }
  .card--white{background:var(--card-white)}
  .card--frost{background:var(--card-frost);opacity:.93}
  .card--tl{left:72px;top:68px}
  .card--tr{left:667px;top:68px}
  .card--bl{left:72px;top:400px}
  .card--br{left:667px;top:400px}

  .card__top{flex:0 0 142px;display:flex;align-items:center;justify-content:center}
  .brand{display:flex;align-items:center;gap:9px}
  .brand__dot{width:22px;height:22px;border-radius:50%;background:var(--brand-dot)}
  .brand__name{font-weight:700;font-size:25px;color:var(--brand);letter-spacing:.5px}

  .card__band{
    flex:1;position:relative;
    background:linear-gradient(180deg,var(--blue-light) 0%,var(--blue-mid) 45%,var(--blue-dark) 100%);
    border-top:4px solid var(--silver);
    color:var(--text-light);
  }
  .name-row{
    height:36px;display:flex;align-items:center;justify-content:center;gap:8px;
    background:rgba(0,0,0,.14);font-size:11px;letter-spacing:.4px;
    border-bottom:1px solid rgba(255,255,255,.25);
  }
  .name-row__name{font-weight:700}
  .name-row__sep{opacity:.8}
  .contact{padding:20px 24px 0;display:flex;flex-direction:column;gap:10px;font-size:8.5px}
  .contact__row{display:flex;gap:18px;align-items:center}
  .contact__item{display:flex;align-items:center;gap:5px;white-space:nowrap}
  .icon{width:11px;height:11px;flex:0 0 11px}

  .web{position:absolute;left:0;right:0;top:50%;transform:translateY(-50%);text-align:center;
    font-size:10px;letter-spacing:5px}
</style>
</head>
<body>

<section class="card card--white card--tl">
  <div class="card__top">
    <div class="brand"><span class="brand__dot"></span><span class="brand__name">BLUE LEDGER PLUS</span></div>
  </div>
  <div class="card__band">
    <div class="name-row"><span class="name-row__name">HAROLD QUINCE</span><span class="name-row__sep">|</span><span>Manger</span></div>
    <div class="contact">
      <div class="contact__row">
        <span class="contact__item"><svg class="icon" viewBox="0 0 12 12"><circle cx="6" cy="6" r="6" fill="#fff"/><path d="M6 2.5a2.2 2.2 0 0 0-2.2 2.2C3.8 6.5 6 9.5 6 9.5s2.2-3 2.2-4.8A2.2 2.2 0 0 0 6 2.5z" fill="#1d6fc8"/></svg>3710 S Wexford st 204 Fairbrook ST 00000</span>
        <span class="contact__item"><svg class="icon" viewBox="0 0 12 12"><circle cx="6" cy="6" r="6" fill="#fff"/><circle cx="6" cy="6" r="3.2" fill="none" stroke="#1d6fc8"/><path d="M2.8 6h6.4M6 2.8v6.4" stroke="#1d6fc8" stroke-width=".8"/></svg>www.BLUELEDGERPLUS.example</span>
      </div>
      <div class="contact__row">
        <span class="contact__item"><svg class="icon" viewBox="0 0 12 12"><circle cx="6" cy="6" r="6" fill="#fff"/><path d="M4 3h1.5l.6 1.6-.9.6a4 4 0 0 0 1.6 1.6l.6-.9L9 6.5V8c-3 .3-5.3-2-5-5z" fill="#1d6fc8"/></svg>555-010-2234</span>
        <span class="contact__item"><svg class="icon" viewBox="0 0 12 12"><circle cx="6" cy="6" r="6" fill="#fff"/><path d="M4 3h1.5l.6 1.6-.9.6a4 4 0 0 0 1.6 1.6l.6-.9L9 6.5V8c-3 .3-5.3-2-5-5z" fill="#1d6fc8"/></svg>555-010-7781</span>
        <span class="contact__item"><svg class="icon" viewBox="0 0 12 12"><circle cx="6" cy="6" r="6" fill="#fff"/><rect x="3" y="4" width="6" height="4" fill="none" stroke="#1d6fc8" stroke-width=".8"/><path d="M3 4l3 2.2L9 4" fill="none" stroke="#1d6fc8" stroke-width=".8"/></svg>BlueLEDGERPLUS@mailnook.example</span>
      </div>
    </div>
  </div>
</section>

<section class="card card--frost card--tr">
  <div class="card__top">
    <div class="brand"><span class="brand__dot"></span><span class="brand__name">BLUE LEDGER PLUS</span></div>
  </div>
  <div class="card__band">
    <div class="name-row"><span class="name-row__name">DENNIS HOLTBERG</span><span class="name-row__sep">|</span><span>Manger</span></div>
    <div class="contact">
      <div class="contact__row">
        <span class="contact__item"><svg class="icon" viewBox="0 0 12 12"><circle cx="6" cy="6" r="6" fill="#fff"/><path d="M6 2.5a2.2 2.2 0 0 0-2.2 2.2C3.8 6.5 6 9.5 6 9.5s2.2-3 2.2-4.8A2.2 2.2 0 0 0 6 2.5z" fill="#1d6fc8"/></svg>3710 S Wexford st 204 Fairbrook ST 00000</span>
        <span class="contact__item"><svg class="icon" viewBox="0 0 12 12"><circle cx="6" cy="6" r="6" fill="#fff"/><circle cx="6" cy="6" r="3.2" fill="none" stroke="#1d6fc8"/><path d="M2.8 6h6.4M6 2.8v6.4" stroke="#1d6fc8" stroke-width=".8"/></svg>www.BLUELEDGERPLUS.example</span>
      </div>
      <div class="contact__row">
        <span class="contact__item"><svg class="icon" viewBox="0 0 12 12"><circle cx="6" cy="6" r="6" fill="#fff"/><path d="M4 3h1.5l.6 1.6-.9.6a4 4 0 0 0 1.6 1.6l.6-.9L9 6.5V8c-3 .3-5.3-2-5-5z" fill="#1d6fc8"/></svg>555-010-2234</span>
        <span class="contact__item"><svg class="icon" viewBox="0 0 12 12"><circle cx="6" cy="6" r="6" fill="#fff"/><path d="M4 3h1.5l.6 1.6-.9.6a4 4 0 0 0 1.6 1.6l.6-.9L9 6.5V8c-3 .3-5.3-2-5-5z" fill="#1d6fc8"/></svg>555-010-7781</span>
        <span class="contact__item"><svg class="icon" viewBox="0 0 12 12"><circle cx="6" cy="6" r="6" fill="#fff"/><rect x="3" y="4" width="6" height="4" fill="none" stroke="#1d6fc8" stroke-width=".8"/><path d="M3 4l3 2.2L9 4" fill="none" stroke="#1d6fc8" stroke-width=".8"/></svg>BlueLEDGERPLUS@mailnook.example</span>
      </div>
    </div>
  </div>
</section>

<section class="card card--white card--bl">
  <div class="card__top">
    <div class="brand"><span class="brand__dot"></span><span class="brand__name">BLUE LEDGER PLUS</span></div>
  </div>
  <div class="card__band"><div class="web">www.BLUELEDGERPLUS.example</div></div>
</section>

<section class="card card--frost card--br">
  <div class="card__top">
    <div class="brand"><span class="brand__dot"></span><span class="brand__name">BLUE LEDGER PLUS</span></div>
  </div>
  <div class="card__band"><div class="web">www.BLUELEDGERPLUS.example</div></div>
</section>

</body>
</html>
```